The Pixel Tap Business card.

A Simple card with our Logo and contact information. To give to investors and other professionals.

We are a nerd themed bar.
our target market is young professionals age 21+ but the real purpose of this business card is to present to potential investors and other professionals with our contact information. as we are still looking for funding before we start up.

I am partial to green and my partner likes red we are open to iteration.

Target Market(s)

Investors

Industry/Entity Type

Business

Contact Information for Business Card

Martin Hale (225) 730-6192 kent.h4711@mailnest.test Glen Porter (225) 968-5037 glenp318@mailnest.test

Font styles to use
Serif

Requirements
Nice to have
• Keep it simple but not boring.
• Use the Logos but feel free to edit them to match theme/colors.
• Keep the back clean and use one of the Logos.

```html
<!DOCTYPE html>
<html lang="en">
<head>
<meta charset="utf-8">
<title>The Pixel Tap – Business Card</title>
<link rel="stylesheet" href="https://fonts.googleapis.com/css2?family=Arimo:wght@400;700&display=swap">
<style>
  :root {
    --backdrop: #d9d6d2;
    --card: #4a4b4d;
    --ink: #0b0b0b;
    --accent: #e0141c;
    --text-light: #f2f2f2;
    --rule: #bdbdbd;
  }
  html, body {
    margin: 0;
    padding: 0;
    width: 1200px;
    height: 787px;
    overflow: hidden;
    background: var(--backdrop);
    font-family: "Arimo", Arial, sans-serif;
  }
  .canvas {
    position: relative;
    width: 1200px;
    height: 787px;
  }
  .card {
    position: absolute;
    top: 250px;
    width: 500px;
    height: 286px;
    background: var(--card);
    border-radius: 3px;
    box-shadow: 0 6px 18px rgba(0,0,0,0.25);
    overflow: hidden;
  }
  .card--back { left: 70px; }
  .card--front { left: 630px; }

  .brand {
    position: absolute;
    display: flex;
    align-items: center;
    gap: 10px;
  }
  .brand__dot {
    width: 22px;
    height: 22px;
    border-radius: 50%;
    background: var(--accent);
    flex: none;
  }
  .brand__name {
    font-weight: 700;
    font-size: 30px;
    line-height: 1;
    letter-spacing: 1px;
    color: var(--ink);
    text-transform: uppercase;
    white-space: nowrap;
  }
  .card--back .brand { left: 140px; top: 150px; }
  .card--front .brand { left: 180px; top: 90px; }

  .holder {
    position: absolute;
    right: 232px;
    top: 170px;
    font-size: 18px;
    font-weight: 700;
    color: var(--accent);
    white-space: nowrap;
  }
  .divider {
    position: absolute;
    left: 282px;
    top: 168px;
    width: 1px;
    height: 64px;
    background: var(--rule);
  }
  .contacts {
    position: absolute;
    left: 296px;
    top: 180px;
    margin: 0;
    padding: 0;
    list-style: none;
    font-size: 15px;
    color: var(--text-light);
  }
  .contacts__item {
    display: flex;
    align-items: center;
    gap: 8px;
    height: 24px;
    white-space: nowrap;
  }
  .contacts__icon {
    width: 14px;
    height: 14px;
    flex: none;
  }
</style>
</head>
<body>
<main class="canvas">
  <section class="card card--back" aria-label="Card back">
    <div class="brand">
      <span class="brand__dot"></span>
      <span class="brand__name">The Pixel Tap</span>
    </div>
  </section>

  <section class="card card--front" aria-label="Card front">
    <div class="brand">
      <span class="brand__dot"></span>
      <span class="brand__name">The Pixel Tap</span>
    </div>
    <div class="holder">Martin Hale</div>
    <div class="divider"></div>
    <ul class="contacts">
      <li class="contacts__item">
        <svg class="contacts__icon" viewBox="0 0 14 14" aria-hidden="true">
          <rect x="3" y="0" width="8" height="14" rx="1.6" fill="var(--accent)"/>
          <rect x="4.3" y="2" width="5.4" height="8" fill="var(--card)"/>
          <circle cx="7" cy="12" r="0.9" fill="var(--card)"/>
        </svg>
        <span>(225) 730-6192</span>
      </li>
      <li class="contacts__item">
        <svg class="contacts__icon" viewBox="0 0 14 14" aria-hidden="true">
          <rect x="0.5" y="2.5" width="13" height="9" rx="1" fill="var(--accent)"/>
          <path d="M1 3 L7 8 L13 3" fill="none" stroke="var(--card)" stroke-width="1.2"/>
        </svg>
        <span>kent.h4711@mailnest.test</span>
      </li>
    </ul>
  </section>
</main>
</body>
</html>
```